Brickpress Design for a website design company

Web Design for a Web Design Company - As odd as that sounds, it is exactly right. We are a website design company with over 120 regular clients, we want to redesign our current website and take it to the next level. The problem we are finding is that we are too "inside the box". Which is why we are looking outside for a designer that will take us to the next level. We need this design to look STATE OF THE ART! Obviously there is allot we can do internally once we have a completed design to wrap up the project. So what we are looking for are some design concepts based on some ideas that we will provide. Once the concept is finalized we will need the layered design and any graphics that were used in separate files. If you have any questions please send them to us privately.

Example websites of how we want to look are:

1. http://www.brivlo.example
2. http://www.plumtavern.example
3. http://zelvaworks.example
4. http://www.kup.example
5. http://www.tarnleaf.example

Our current website we are redesigning is: www.frostlanewd.example

Navigation / Pages for new website are as follows:

Home
Services (page with broad detailing)
Portfolio
RFQ
Testimonials
About
Contact

Website Design
Website Re-design
Ecommerce
Mobile Websites
Copywriting
Hosting and Maintenance
Content Marketing
Pay Per Click Marketing
Mobile Text Marketing
Local Search Marketing

Design must be brickpress compatible, we use the meridian framework specifically.
Target Market(s)
Our target market is B2B, we want to sell web and marketing products
Requirements
Must Have:
- Design must be brickpress compatible, we use the meridian framework specifically.

As a bonus, if we like your work we may use you for our own clients...

Marcus

Industry/Entity Type

Marketing

Requirements
Must have
• For the content area - intro paragraph and blog categories below the header/banner area,

Need to include both shaded content "buttons" with graphics similar to the website attached jpg file titled - bottom content area

and hanging shaded ribbons from pixvault.example - attached jpg file titled: stock-illustration-57310268-glossy-promoting-badges

```html
<!DOCTYPE html>
<html lang="en">
<head>
<meta charset="utf-8">
<title>FrostLane Website Design</title>
<link rel="stylesheet" href="https://fonts.googleapis.com/css2?family=Ubuntu:ital,wght@0,300;0,400;0,500;0,700;1,500;1,700&family=Ubuntu+Condensed&display=swap">
<style>
:root{
  --sky-top:#c9e6f1;
  --sky-low:#e3f2f7;
  --ink:#3c3c3c;
  --muted:#7c7f83;
  --orange:#f39a1e;
  --orange-deep:#ee6b12;
  --red:#d8281c;
  --blue:#1383cf;
  --blue-light:#3fa5e0;
  --green:#6cc21a;
  --yellow:#f3e21b;
  --c1:#edb31a;
  --c2:#b9cc33;
  --c3:#5aa8cf;
  --c4:#9077be;
  --c5:#f39a1e;
}
*{margin:0;padding:0;box-sizing:border-box}
html,body{width:1186px;height:1200px;overflow:hidden}
body{
  position:relative;
  font-family:"Ubuntu",sans-serif;
  color:var(--ink);
  background:
    radial-gradient(ellipse 260px 90px at 130px 300px,rgba(255,255,255,.75),transparent),
    radial-gradient(ellipse 220px 80px at 110px 600px,rgba(255,255,255,.7),transparent),
    radial-gradient(ellipse 260px 90px at 1060px 200px,rgba(255,255,255,.75),transparent),
    radial-gradient(ellipse 240px 90px at 1080px 620px,rgba(255,255,255,.7),transparent),
    radial-gradient(ellipse 420px 360px at 593px 520px,rgba(255,255,255,.75),transparent),
    linear-gradient(180deg,var(--sky-top),var(--sky-low) 60%,#d6edf5);
}
.abs{position:absolute}

/* header */
.brand{left:198px;top:70px;font-size:30px;font-weight:400;color:#2f2f2f;line-height:1}
.social{left:703px;top:38px;display:flex;gap:4px}
.social span{width:16px;height:16px;border-radius:50%;background:var(--blue)}
.call{left:800px;top:28px;display:flex;align-items:center;gap:6px}
.call small{display:block;font-size:11px;color:var(--muted)}
.call strong{font-weight:400;font-size:14px;color:#333}
.call strong em{font-style:normal;color:var(--orange);font-size:15px;margin-left:4px}
.nav{left:475px;top:100px;display:flex;font-size:12px;letter-spacing:.3px}
.nav a{text-decoration:none;color:#333}
.nav a.current{color:var(--orange)}
.nav i{font-style:normal;margin:0 10px;color:#555}

/* hero */
.bubbles{left:0;top:0}
.bubble-title{font-family:"Ubuntu Condensed",sans-serif;font-size:13px}
.headline{left:0;top:560px}
.rule{left:197px;width:792px;border-top:2px dashed rgba(150,160,165,.45)}

/* welcome */
.welcome{left:190px;top:700px}
.welcome-divider{left:374px;top:690px;height:64px;border-left:1px dashed #9aa}
.intro{left:384px;top:689px;width:606px;font-size:9.3px;line-height:13px;color:#666}
.intro p+p{margin-top:4px}

/* ribbons */
.ribbon{position:absolute;top:772px;width:112px;height:336px;border-radius:56px;
  background:repeating-linear-gradient(90deg,rgba(255,255,255,.07) 0 2px,transparent 2px 4px),var(--tone);
  box-shadow:inset 0 -10px 16px rgba(0,0,0,.12);color:#fff;text-align:center}
.ribbon::after{content:"";position:absolute;left:10px;right:10px;bottom:-22px;height:10px;border-radius:50%;background:rgba(60,90,110,.18);filter:blur(3px)}
.ribbon .badge{position:absolute;left:0;top:0;width:112px;height:112px;border-radius:50%;background:rgba(255,255,255,.45);display:flex;align-items:center;justify-content:center}
.ribbon .num{width:86px;height:86px;border-radius:50%;background:radial-gradient(circle at 50% 40%,rgba(255,255,255,.25),rgba(0,0,0,.1)),var(--tone);
  box-shadow:inset 0 0 0 5px rgba(0,0,0,.08);display:flex;align-items:center;justify-content:center;
  font-family:"Ubuntu Condensed",sans-serif;font-size:34px;font-weight:700;text-shadow:0 2px 2px rgba(0,0,0,.3)}
.ribbon .copy{position:absolute;left:14px;right:12px;top:127px;text-align:left;font-size:8.4px;line-height:9.6px}
.ribbon .sep{position:absolute;left:14px;right:14px;top:224px;border-top:1px dotted rgba(255,255,255,.6)}
.ribbon .label{position:absolute;left:0;right:0;top:234px;font-size:10px;font-weight:700;font-style:italic;color:#4a4a4a;line-height:10px;letter-spacing:-.3px}
.ribbon .dots{position:absolute;left:0;right:0;top:256px;display:flex;justify-content:center;gap:3px}
.ribbon .dots span{width:6px;height:6px;border-radius:50%;background:#fff}
.ribbon svg.icon{position:absolute;left:36px;top:272px}
.r1{left:197px;--tone:var(--c1)}
.r2{left:367px;--tone:var(--c2)}
.r3{left:540px;--tone:var(--c3)}
.r4{left:710px;--tone:var(--c4)}
.r5{left:876px;--tone:var(--c5)}

/* footer */
.foot-links{left:198px;top:1156px;font-size:10.5px;color:#555}
.copyright{left:198px;top:1175px;font-size:10.5px;color:#888}
.address{left:746px;top:1154px;display:flex;align-items:center;gap:6px;font-size:10.5px;color:#555}
</style>
</head>
<body>

<header>
  <div class="abs brand">FrostLane</div>
  <div class="abs social" aria-label="Social links"><span></span><span></span><span></span><span></span></div>
  <div class="abs call">
    <svg width="24" height="24" viewBox="0 0 24 24" aria-hidden="true"><path d="M5 2c1 0 3 3 3 4s-2 2-2 3 4 7 6 7 2-2 3-2 4 2 4 3-2 4-4 4C9 21 2 12 2 6 2 4 4 2 5 2z" fill="var(--orange)"/></svg>
    <div><small>Free Consultation</small><strong>Call Now<em>555.014.2291</em></strong></div>
  </div>
  <nav class="abs nav">
    <a class="current" href="#">HOME</a><i>|</i><a href="#">SERVICES</a><i>|</i><a href="#">PORTFOLIO</a><i>|</i><a href="#">RFQ</a><i>|</i><a href="#">TESTIMONIALS</a><i>|</i><a href="#">ABOUT</a><i>|</i><a href="#">CONTACT</a>
  </nav>
</header>

<svg class="abs bubbles" width="1186" height="560" viewBox="0 0 1186 560" aria-label="Service bubbles">
  <defs>
    <radialGradient id="face" cx="45%" cy="40%" r="60%">
      <stop offset="0" stop-color="#fff"/><stop offset=".75" stop-color="#fbfbfb"/><stop offset="1" stop-color="#e4e6e8"/>
    </radialGradient>
  </defs>
  <g fill="url(#face)">
    <circle cx="462" cy="312" r="47" stroke="var(--red)" stroke-width="9"/>
    <circle cx="430" cy="420" r="66" stroke="var(--blue-light)" stroke-width="11"/>
    <circle cx="338" cy="338" r="80" stroke="var(--orange-deep)" stroke-width="15"/>
    <circle cx="574" cy="364" r="56" stroke="var(--green)" stroke-width="11"/>
    <circle cx="792" cy="316" r="150" stroke="var(--blue)" stroke-width="20"/>
    <circle cx="472" cy="388" r="54" stroke="var(--orange-deep)" stroke-width="11"/>
    <circle cx="454" cy="478" r="32" stroke="var(--yellow)" stroke-width="7"/>
    <circle cx="546" cy="476" r="59" stroke="var(--blue)" stroke-width="12"/>
    <circle cx="676" cy="448" r="76" stroke="var(--yellow)" stroke-width="15"/>
  </g>

  <g fill="none" stroke="var(--orange-deep)" stroke-width="2.5">
    <path d="M326 290h5l4 15h14l3-10h-18"/>
    <circle cx="337" cy="310" r="2" fill="var(--orange-deep)"/><circle cx="348" cy="310" r="2" fill="var(--orange-deep)"/>
  </g>
  <text x="338" y="330" text-anchor="middle" class="bubble-title" fill="var(--orange-deep)">ECOMMERCE</text>
  <text x="338" y="344" text-anchor="middle" font-size="8.5" fill="var(--orange-deep)">Lorem ipsum dolor sit</text>
  <text x="338" y="354" text-anchor="middle" font-size="8.5" fill="var(--orange-deep)">amet, consectetuer</text>

  <g fill="none" stroke="var(--orange)" stroke-width="2">
    <rect x="462" y="356" width="20" height="8"/><rect x="462" y="364" width="20" height="8"/><path d="M472 372v4M464 377h16"/>
  </g>
  <text x="472" y="394" text-anchor="middle" class="bubble-title" fill="var(--orange)">HOSTING</text>
  <text x="472" y="406" text-anchor="middle" font-size="8" fill="var(--orange)">Lorem ipsum</text>
  <text x="472" y="415" text-anchor="middle" font-size="8" fill="var(--orange)">dolor sit amet,</text>

  <path d="M560 356l20-20 6 20z" fill="var(--green)"/><path d="M562 356h10v5h-10z" fill="var(--green)"/>
  <text x="578" y="376" text-anchor="middle" class="bubble-title" fill="var(--green)">MARKETING</text>

  <ellipse cx="790" cy="245" rx="30" ry="44" transform="rotate(-30 790 245)" fill="var(--blue)" opacity=".85" role="img" aria-label="Feather quill illustration"/>
  <text x="792" y="318" text-anchor="middle" font-family="Ubuntu Condensed,sans-serif" font-size="15" fill="var(--blue)">WEBSITE DESIGN</text>
  <text x="792" y="333" text-anchor="middle" font-size="8.5" fill="var(--blue)">Lorem ipsum dolor sit amet, consectetuer adipiscing</text>
  <text x="792" y="345" text-anchor="middle" font-size="8.5" fill="var(--blue)">elit, sed diam nonummy nibh euismod tincidunt ut</text>
  <text x="792" y="357" text-anchor="middle" font-size="8.5" fill="var(--blue)">laoreet dolore magna aliquam erat volutpat.</text>

  <rect x="538" y="438" width="16" height="24" rx="2" fill="var(--blue)"/><rect x="541" y="442" width="10" height="6" fill="#fff"/>
  <text x="546" y="480" text-anchor="middle" class="bubble-title" fill="var(--blue)">MOBILE APP</text>
  <text x="546" y="493" text-anchor="middle" font-size="8.5" fill="var(--blue)">Lorem ipsum dolor sit</text>
  <text x="546" y="503" text-anchor="middle" font-size="8.5" fill="var(--blue)">amet, consectetuer</text>

  <g fill="none" stroke="#f1c40f" stroke-width="2"><rect x="654" y="406" width="22" height="28" rx="2"/><path d="M670 430l14-14 4 4-14 14h-4z"/></g>
  <text x="670" y="458" text-anchor="middle" class="bubble-title" fill="#f1c40f">COPYWRITING</text>
  <text x="670" y="471" text-anchor="middle" font-size="8.5" fill="#f1c40f">Lorem ipsum dolor sit</text>
  <text x="670" y="481" text-anchor="middle" font-size="8.5" fill="#f1c40f">amet, consectetuer</text>
</svg>

<section>
  <svg class="abs headline" width="1186" height="100" viewBox="0 560 1186 100" aria-label="Creative, innovative websites, so you can turn dreams into businesses">
    <text x="300" y="636" font-family="Ubuntu Condensed,sans-serif" font-size="28" fill="var(--orange)" textLength="112" lengthAdjust="spacingAndGlyphs">CREATIVE,</text>
    <text x="422" y="636" font-family="Ubuntu Condensed,sans-serif" font-size="28" fill="var(--blue)" textLength="143" lengthAdjust="spacingAndGlyphs">INNOVATIVE</text>
    <text x="566" y="634" font-family="Ubuntu Condensed,sans-serif" font-size="72" fill="var(--orange)" textLength="324" lengthAdjust="spacingAndGlyphs">WEBSITES</text>
    <text x="578" y="654" font-family="Ubuntu,sans-serif" font-size="13" fill="var(--muted)" textLength="311" lengthAdjust="spacingAndGlyphs">SO YOU CAN TURN DREAMS INTO BUSINESSES</text>
  </svg>
  <div class="abs rule" style="top:672px"></div>

  <svg class="abs welcome" width="180" height="50" viewBox="190 700 180 50">
    <text x="222" y="734" font-family="Ubuntu Condensed,sans-serif" font-size="32" fill="#6a6a6a" textLength="140" lengthAdjust="spacingAndGlyphs">WELCOME</text>
  </svg>
  <div class="abs welcome-divider"></div>
  <div class="abs intro">
    <p>FrostLane, a leading professional web design and web development company operating out of Ashgrove county in northeastern Pennsylvania, serves businesses everywhere...from down the street to across the country. No matter what your web needs might be, or the industry you service.</p>
    <p>Whether it's a brand new website or the redesign of an existing one, you have the power to establish... an appealing and effective presence on the web. Not only will your creations through FrostLane look sensational...</p>
  </div>
</section>

<section class="ribbons">
  <article class="ribbon r1">
    <div class="badge"><div class="num">01</div></div>
    <p class="copy">Lorem Ipsum is simply dummy text of the printing and typesetting industry. Lorem Ipsum has been the industry's standard dummy text ever since the 1500s, when an unknown...</p>
    <div class="sep"></div><div class="label">WEB DESIGN</div>
    <div class="dots"><span></span></div>
    <svg class="icon" width="40" height="40" viewBox="0 0 40 40" aria-hidden="true"><path d="M8 32l4-8 18-16 3 3-16 18z" fill="#fff"/><path d="M4 36h10" stroke="#fff" stroke-width="2"/></svg>
  </article>
  <article class="ribbon r2">
    <div class="badge"><div class="num">02</div></div>
    <p class="copy">Lorem Ipsum is simply dummy text of the printing and typesetting industry. Lorem Ipsum has been the industry's standard dummy text ever since the 1500s, when an unknown...</p>
    <div class="sep"></div><div class="label">WEB<br>DEVELOPMENT</div>
    <div class="dots"><span></span><span></span></div>
    <svg class="icon" width="40" height="40" viewBox="0 0 40 40" aria-hidden="true"><circle cx="15" cy="22" r="9" fill="none" stroke="#fff" stroke-width="5" stroke-dasharray="4 3"/><path d="M18 30l16-16 3 3-16 16h-3z" fill="#fff"/></svg>
  </article>
  <article class="ribbon r3">
    <div class="badge"><div class="num">03</div></div>
    <p class="copy">Lorem Ipsum is simply dummy text of the printing and typesetting industry. Lorem Ipsum has been the industry's standard dummy text ever since the 1500s, when an unknown...</p>
    <div class="sep"></div><div class="label" style="top:244px">E-COMMERCE</div>
    <div class="dots" style="top:260px"><span></span><span></span><span></span></div>
    <svg class="icon" width="40" height="40" viewBox="0 0 40 40" aria-hidden="true"><path d="M6 18h28l-4 16H10z" fill="#fff"/><path d="M12 18l8-10 8 10" fill="none" stroke="#fff" stroke-width="2.5"/></svg>
  </article>
  <article class="ribbon r4">
    <div class="badge"><div class="num">04</div></div>
    <p class="copy">Lorem Ipsum is simply dummy text of the printing and typesetting industry. Lorem Ipsum has been the industry's standard dummy text ever since the 1500s, when an unknown...</p>
    <div class="sep"></div><div class="label" style="top:244px">BRANDING</div>
    <div class="dots" style="top:260px"><span></span><span></span><span></span><span></span></div>
    <svg class="icon" width="40" height="40" viewBox="0 0 40 40" aria-hidden="true"><path d="M4 24L22 6h10v10L14 34z" fill="#fff"/><circle cx="27" cy="11" r="2.5" fill="var(--c4)"/></svg>
  </article>
  <article class="ribbon r5">
    <div class="badge"><div class="num">05</div></div>
    <p class="copy">Lorem Ipsum is simply dummy text of the printing and typesetting industry. Lorem Ipsum has been the industry's standard dummy text ever since the 1500s, when an unknown...</p>
    <div class="sep"></div><div class="label" style="top:244px">MARKETING</div>
    <div class="dots" style="top:260px"><span></span><span></span><span></span><span></span><span></span></div>
    <svg class="icon" width="40" height="40" viewBox="0 0 40 40" aria-hidden="true"><rect x="6" y="22" width="7" height="14" fill="#fff"/><rect x="16" y="15" width="7" height="21" fill="#fff"/><rect x="26" y="6" width="7" height="30" fill="#fff"/></svg>
  </article>
</section>

<footer>
  <div class="abs rule" style="top:1142px"></div>
  <div class="abs foot-links">FrostLane &nbsp;- Services - Portfolio &nbsp;- &nbsp;Contact Us &nbsp;- &nbsp;Request A Quote &nbsp;- &nbsp;Associates</div>
  <div class="abs copyright">© 2013 FrostLane Website Design</div>
  <div class="abs address">
    <svg width="12" height="16" viewBox="0 0 12 16" aria-hidden="true"><path d="M6 0a6 6 0 0 1 6 6c0 4-6 10-6 10S0 10 0 6a6 6 0 0 1 6-6z" fill="var(--orange)"/><circle cx="6" cy="6" r="2.2" fill="#fff"/></svg>
    Twelve Orchard Row - Millbrook, PA 17000
  </div>
</footer>

</body>
</html>
```